Signage setout with photos for side of Mowing Trailer

We need signage for our mowing trailer to attract new business.
Specifically a Rear sign 1470x880mm and Side signs 2400x880mm
Sign needs to be modern and professional.
Some example uploads as to what we have thought about so far.
Logo doesn't need to be the green colour.
Logo words and Logo of Mower do not need to be together.
Link to get a mower image>
https://bluefernmachinery.com/torvo
Updates

Need extra days to review

Target Market(s)

Other Customers driving past the trailer.

Industry/Entity Type

Lawnmowing / Landscaping

Requirements
Must have
• Phone Number, Company Name & Logo, Web address, Chatbook and Insta Logos, Comment - "Acreage & Commercial Specialists" Catchcry - "100% Electric Mowing Company - est 2017" Services "Mowing, Hedging, Pressure Cleaning, Weed Control, Fencing, Turfing, Mulching and Rubbish Removal"
Nice to have
• Full colour background images.

```html
<!DOCTYPE html>
<html lang="en">
<head>
<meta charset="utf-8">
<title>Fresh Blade Mowing – Trailer Sign</title>
<link href="https://fonts.googleapis.com/css2?family=Oswald:wght@400;500;600&family=Mukta:wght@700&display=swap" rel="stylesheet">
<style>
  :root {
    --sky-top: #5aa9e6;
    --sky-low: #a8d3f0;
    --tree: #4f7a3a;
    --grass: #5fae2f;
    --grass-deep: #3f8f1f;
    --mower: #6fd23a;
    --orange: #e8652a;
    --white: #ffffff;
    --shadow-green: #1f5a14;
  }
  * { margin: 0; padding: 0; box-sizing: border-box; }
  html, body { width: 1200px; height: 726px; overflow: hidden; background: #fff; }
  .sign {
    position: relative;
    width: 1200px;
    height: 726px;
    overflow: hidden;
    font-family: "Oswald", sans-serif;
    color: var(--white);
  }
  .scene-backdrop {
    position: absolute; inset: 0;
    background: linear-gradient(180deg, var(--sky-top) 0%, var(--sky-low) 25%, var(--tree) 42%, var(--grass) 55%, var(--grass-deep) 100%);
  }
  .mower-photo {
    position: absolute;
    left: 384px; top: 78px; width: 480px; height: 357px;
    background: radial-gradient(ellipse at 55% 70%, var(--mower) 0%, #4aa82a 45%, rgba(63,143,31,0) 75%);
  }
  .brand {
    position: absolute; left: 30px; top: 34px; width: 360px;
    text-align: center;
  }
  .brand-mark {
    width: 100px; height: 100px; border-radius: 50%;
    background: var(--orange);
    margin: 0 auto 40px;
  }
  .brand-name {
    font-family: "Mukta", sans-serif;
    font-weight: 700;
    color: var(--white);
    line-height: 1;
    white-space: nowrap;
  }
  .brand-name .line1 { display: block; font-size: 50px; }
  .brand-name .line2 { display: block; font-size: 66px; letter-spacing: 2px; margin-top: 2px; }
  .phone {
    position: absolute; left: 700px; top: 44px; width: 470px;
    font-size: 104px; font-weight: 600; line-height: 1;
    color: var(--orange); text-align: center;
    white-space: nowrap;
    text-shadow: 0 0 3px var(--white), 0 0 3px var(--white), 0 0 4px var(--white);
  }
  .website {
    position: absolute; left: 712px; top: 156px; width: 456px;
    font-size: 32px; font-weight: 400; line-height: 1.1; text-align: center;
    white-space: nowrap;
    text-shadow: 0 2px 3px var(--shadow-green);
  }
  .social {
    position: absolute; left: 870px; top: 238px;
    display: flex; gap: 22px;
    font-size: 24px; font-weight: 500;
  }
  .social-item { display: flex; align-items: center; gap: 8px; text-shadow: 0 2px 3px var(--shadow-green); }
  .social-square { width: 30px; height: 30px; background: var(--white); border-radius: 5px; }
  .tagline {
    position: absolute; left: 0; right: 0; top: 430px;
    text-align: center; font-size: 50px; font-weight: 400; line-height: 1.2;
    text-shadow: 0 2px 4px var(--shadow-green);
  }
  .catchcry {
    position: absolute; left: 52px; top: 500px; width: 1103px; height: 90px;
    background: var(--orange);
    border: 3px solid var(--white);
    border-radius: 46px;
    display: flex; align-items: center; justify-content: center;
    font-size: 62px; font-weight: 600; letter-spacing: 0.5px;
  }
  .services {
    position: absolute; left: 0; right: 0; top: 596px;
    text-align: center; font-size: 43px; font-weight: 400; line-height: 54px;
    text-shadow: 0 2px 4px var(--shadow-green);
    list-style: none;
  }
  .services li { display: inline; margin: 0 8px; }
  .services li::before {
    content: ""; display: inline-block;
    width: 18px; height: 18px; border-radius: 50%;
    background: var(--orange); border: 2px solid var(--white);
    margin-right: 4px; vertical-align: 6px;
  }
</style>
</head>
<body>
<main class="sign">
  <div class="scene-backdrop" role="img" aria-label="Full colour photo of a mown lawn with trees and blue sky behind"></div>
  <div class="mower-photo" role="img" aria-label="Photo of an operator riding a green electric zero-turn mower"></div>

  <div class="brand">
    <div class="brand-mark"></div>
    <div class="brand-name"><span class="line1">FRESH BLADE</span><span class="line2">MOWING</span></div>
  </div>

  <div class="phone">3555 0142</div>
  <div class="website">www.freshblademowing.com.au</div>
  <div class="social">
    <span class="social-item"><span class="social-square"></span>Chatbook</span>
    <span class="social-item"><span class="social-square"></span>Snapgram</span>
  </div>

  <p class="tagline">Acreage &amp; Commercial Specialists</p>
  <div class="catchcry">100% Electric Mowing Company - est 2017</div>

  <ul class="services">
    <li>Services "Mowing</li><li>Hedging</li><li>Pressure Cleaning</li><br>
    <li>Weed Control</li><li>Fencing</li><li>Turfing</li><li>Mulching and Rubbish Removal</li>
  </ul>
</main>
</body>
</html>
```